business card design for luxurious real estate brand

using the attached logo, i am looking for a 2-sided business card design. the back should be the gold logo on black background. the front needs to include: gold logo, name, phone, email, and website

Industry/Entity Type

real estate

Contact Information for Business Card

logo, name, email, phone, website

Font styles to use
Sans Serif

```html
<!DOCTYPE html>
<html lang="en">
<head>
<meta charset="UTF-8">
<title>Casa Ridgeway – Business Card</title>
<link href="https://fonts.googleapis.com/css2?family=Arimo:wght@400;700&display=swap" rel="stylesheet">
<style>
  :root {
    --backdrop: #2d2d2d;
    --card: #000000;
    --gold: #ffcc08;
    --white: #ffffff;
  }
  * { margin: 0; padding: 0; box-sizing: border-box; }
  html, body {
    width: 1200px;
    height: 1015px;
    overflow: hidden;
    background: var(--backdrop);
    font-family: "Arimo", Arial, sans-serif;
  }
  .card {
    position: absolute;
    left: 240px;
    width: 720px;
    height: 410px;
    background: var(--card);
    box-shadow: 0 18px 30px rgba(0,0,0,0.45);
  }
  .card--back { top: 70px; }
  .card--front { top: 535px; }

  /* Back side */
  .back-brand {
    position: absolute;
    inset: 0;
    display: flex;
    align-items: center;
    justify-content: center;
    gap: 22px;
  }
  .brand-square {
    width: 34px;
    height: 34px;
    background: var(--gold);
  }
  .back-brand__name {
    color: var(--gold);
    font-size: 34px;
    font-weight: 400;
    letter-spacing: 0.32em;
  }

  /* Front side */
  .front-brand {
    position: absolute;
    right: 54px;
    top: 70px;
    display: flex;
    align-items: center;
    gap: 16px;
  }
  .front-brand__name {
    color: var(--gold);
    font-size: 40px;
    font-weight: 700;
    letter-spacing: 0.04em;
    line-height: 1.05;
    text-align: right;
  }
  .contact {
    position: absolute;
    left: 60px;
    top: 150px;
    color: var(--white);
  }
  .contact__name {
    color: var(--gold);
    font-size: 22px;
    font-weight: 700;
    line-height: 1;
  }
  .contact__title {
    margin-top: 4px;
    font-size: 15px;
    letter-spacing: 0.02em;
  }
  .rule {
    width: 150px;
    height: 1px;
    background: var(--gold);
    margin: 18px 0 16px 0;
  }
  .contact__list { list-style: none; }
  .contact__list li {
    display: flex;
    align-items: center;
    gap: 10px;
    font-size: 17px;
    line-height: 24px;
  }
  .contact__list svg { width: 16px; height: 16px; flex: none; }
  .contact__address {
    font-size: 17px;
    line-height: 23px;
  }
</style>
</head>
<body>

<section class="card card--back" aria-label="Card back">
  <div class="back-brand">
    <span class="brand-square"></span>
    <span class="back-brand__name">CASA RIDGEWAY</span>
  </div>
</section>

<section class="card card--front" aria-label="Card front">
  <div class="front-brand">
    <span class="front-brand__name">CASA<br>RIDGEWAY</span>
    <span class="brand-square"></span>
  </div>

  <div class="contact">
    <h1 class="contact__name">MARCUS HALE</h1>
    <p class="contact__title">MANAGING DIRECTOR</p>
    <div class="rule"></div>
    <ul class="contact__list">
      <li>
        <svg viewBox="0 0 16 16" aria-hidden="true"><path fill="var(--gold)" d="M3.6 1.5l2.3 2.6-1.3 1.6c.9 1.9 2.4 3.4 4.3 4.4l1.6-1.3 2.6 2.3-1.4 2.4C6.4 13.4 2.6 9.6 1.2 2.9z"/></svg>
        055-321 654 987
      </li>
      <li>
        <svg viewBox="0 0 16 16" aria-hidden="true"><rect x="1" y="3" width="14" height="10" fill="var(--gold)"/><path d="M1 3l7 6 7-6" fill="none" stroke="#000" stroke-width="1.2"/></svg>
        hello@casaridgeway.com
      </li>
      <li>
        <svg viewBox="0 0 16 16" aria-hidden="true"><g fill="none" stroke="var(--gold)" stroke-width="1.3"><circle cx="8" cy="8" r="6.5"/><ellipse cx="8" cy="8" rx="3" ry="6.5"/><path d="M1.5 8h13M2.5 4.8h11M2.5 11.2h11"/></g></svg>
        www.casaridgeway.com
      </li>
    </ul>
    <div class="rule"></div>
    <p class="contact__address">88, Harbor Lane, Suite 4<br>20817, Northvale</p>
  </div>
</section>

</body>
</html>
```